IV Nutritional Clinic Web Design

We are working with Velmo. They are an IV Nutritional Clinic and in need of a new website design.
Some sites to use for inspiration:
https://brantlowcare.example
https://www.zolvarihealth.example
https://www.quellspa.example
https://pimrolift.example
https://www.dorvak-well.example/pages/iv-therapy-west-hollywood
https://www.tqoncowell.example/cancer-care/iv-drips/
https://drelmavita.example
https://salbrikmed.example
Thank you for taking the time to consider designing a website for us. We are web developers based in Stockton, CA, USA. Most of our projects go through the same process. Understanding this process may help you win a project with us. We custom-code all of our websites in-house. We don’t have any requirements as to what tools you use for your design, but we prefer Figma files. For any design that we label as four-stars, we send it to the client for review. The client picks the final design they want us to use. Once we complete this process, we will continue to show additional clients all the four-star sites and purchase them later. Your designs will have multiple chances to sell. For better chances of success, we ask that you follow these guidelines.
IMAGES:
If you use any images or icons in the design, we ask that you have a link to the asset so we can purchase the image/icon. Most of the designs we submit do not have the customer’s images on them unless they have some great images. Be creative; show us the feeling you are trying to portray with your image choices. Use any royalty-free site you choose. We subscribe to Corvix and mainly use their images, but we can purchase images outside of Corvix.
PLEASE NOTE: we will not submit designs to clients with watermarks on the images.
FONTS:
We ask that you identify the fonts used in the design. This can be done in a message if you want. We typically use Lumen Typeset and Corvix Fonts.
CONTENT:
We're always open to different content and ideas. We often submit designs with stock images so the client can see our vision. We typically take pictures after the website launch to use their images with our vision. Lorem Ipsum is fine for paragraphs, but we ask that you write the headers in correct English. We want to be able to show the vision and identify the sections of the website.
INSPIRATION:
We typically add a couple of links in the brief of websites we like to help you get started in your design.
REVISIONS:
We do not often ask for revisions of the designs unless we see something in the design that may not appeal to the client. If there are slight changes that we want to make, we do that in the development process.
FEEDBACK:
We rarely give feedback on designs during the design process. We are working on many website projects and do not have the time to provide feedback. We usually respond if your request is well thought out and asks specific questions, but a note asking “feedback, please” usually goes unanswered.
Number of Pages Required
1 page
Look and feel
Each slider illustrates characteristics of the customer's brand and the style your logo design should communicate.

```html
<!DOCTYPE html>
<html lang="en">
<head>
<meta charset="utf-8">
<title>Velmo Hydration – IV Nutrition Clinic</title>
<link href="https://fonts.googleapis.com/css2?family=Ubuntu:wght@400;500;700&family=Open+Sans:wght@400;600;700&display=swap" rel="stylesheet">
<style>
:root{
  --navy:#141a4d;
  --navy-soft:#26366a;
  --green:#79a23a;
  --green-light:#8db43f;
  --grey:#6f6f6f;
  --text:#555a66;
  --light-bg:#e9eef6;
  --card-bg:#f7f6f1;
  --white:#ffffff;
}
*{margin:0;padding:0;box-sizing:border-box}
html,body{width:1200px;height:4066px;overflow:hidden}
body{position:relative;font-family:"Open Sans",sans-serif;color:var(--text);background:var(--white)}
.abs{position:absolute}
.heading{font-family:"Ubuntu",sans-serif;font-weight:700;color:var(--navy);letter-spacing:.2px}
.center{left:0;width:1200px;text-align:center}
.eyebrow{font-size:14px;color:var(--green);text-transform:uppercase;display:inline-block;padding-bottom:6px;border-bottom:1px solid var(--green)}
.btn{position:absolute;display:flex;align-items:center;justify-content:center;gap:14px;font-family:"Open Sans",sans-serif;font-weight:700;color:var(--white);border-radius:4px}
.btn-green{background:var(--green);font-size:16px}

/* top bar */
.topbar{left:0;top:0;width:1200px;height:32px}
.topbar-text{font-size:11px;font-weight:700;color:var(--white);display:flex;align-items:center;gap:8px}
.logo{font-family:"Ubuntu",sans-serif;font-weight:700;color:var(--navy);font-size:40px;letter-spacing:2px;display:flex;align-items:center;gap:10px}
.logo-mark{width:12px;height:12px;background:var(--green)}
.nav a{position:absolute;top:61px;font-size:11px;color:#333;text-decoration:none}
.book{left:932px;top:54px;width:118px;height:30px;border:1.5px solid var(--navy);border-radius:3px;font-size:11px;font-weight:700;color:var(--navy);display:flex;align-items:center;justify-content:center}

/* hero */
.hero-photo{left:0;top:101px;width:1200px;height:673px;
  background:
    linear-gradient(90deg,rgba(243,245,247,.96) 0%,rgba(243,245,247,.8) 30%,rgba(243,245,247,.15) 55%,rgba(243,245,247,0) 70%),
    radial-gradient(ellipse 180px 240px at 40% 35%,rgba(60,120,160,.75),rgba(60,120,160,0)),
    radial-gradient(ellipse 140px 110px at 36% 14%,rgba(214,182,160,.8),rgba(214,182,160,0)),
    radial-gradient(ellipse 170px 150px at 75% 38%,rgba(205,170,150,.85),rgba(205,170,150,0)),
    radial-gradient(ellipse 160px 260px at 89% 58%,rgba(34,132,158,.85),rgba(34,132,158,0)),
    radial-gradient(ellipse 260px 200px at 72% 75%,rgba(215,220,226,.9),rgba(215,220,226,0)),
    linear-gradient(90deg,#eef1f4 0%,#dce4ea 40%,#b8c6d0 70%,#a9b7c1 100%)}
.hero-kicker{left:104px;top:290px;font-family:"Ubuntu",sans-serif;font-size:20px;letter-spacing:6px;color:var(--navy);font-weight:500}
.hero-title{left:98px;top:312px;font-family:"Ubuntu",sans-serif;font-weight:700;font-size:72px;color:var(--navy)}
.hero-rule{left:104px;top:410px;width:488px;height:1px;background:#8a8f99}
.hero-copy{left:104px;top:430px;width:520px;font-size:16.5px;line-height:28px;color:#3e4250}
.btn-pill{position:absolute;top:515px;height:41px;border-radius:21px;font-size:14px;font-weight:700;color:var(--white);display:flex;align-items:center;justify-content:center}

/* about */
.about-photo{left:122px;top:977px;width:497px;height:341px;border-radius:6px;
  background:
    radial-gradient(ellipse 90px 170px at 85% 55%,rgba(58,128,190,.85),rgba(58,128,190,0)),
    radial-gradient(ellipse 70px 60px at 83% 20%,rgba(205,165,140,.8),rgba(205,165,140,0)),
    radial-gradient(ellipse 90px 80px at 25% 55%,rgba(190,150,120,.75),rgba(190,150,120,0)),
    radial-gradient(ellipse 80px 70px at 54% 68%,rgba(210,172,148,.8),rgba(210,172,148,0)),
    radial-gradient(ellipse 120px 100px at 20% 90%,rgba(250,250,252,.95),rgba(250,250,252,0)),
    linear-gradient(135deg,#eef2f4 0%,#dfe6ea 45%,#c9d6de 100%)}
.about-card{left:568px;top:1017px;width:510px;height:281px;background:var(--card-bg);border-radius:6px}
.about-card h3{position:absolute;left:28px;top:40px;font-family:"Ubuntu",sans-serif;font-weight:500;font-size:22px;color:var(--navy)}
.about-card p{position:absolute;left:28px;top:82px;width:450px;font-size:12.6px;line-height:16.8px;color:#7d818c}

/* services */
.services{left:0;top:1410px;width:1200px;height:576px;
  background:
    radial-gradient(ellipse 160px 200px at 12% 30%,rgba(120,110,120,.45),rgba(120,110,120,0)),
    radial-gradient(ellipse 180px 220px at 88% 25%,rgba(150,150,160,.45),rgba(150,150,160,0)),
    radial-gradient(ellipse 150px 180px at 55% 20%,rgba(110,100,110,.35),rgba(110,100,110,0)),
    linear-gradient(90deg,#2b3a6a,#33467a 50%,#2a3a68)}
.svc-card{position:absolute;top:1618px;width:304px;height:228px;overflow:hidden}
.svc-card .shade{position:absolute;inset:0;background:linear-gradient(180deg,rgba(0,0,0,0) 45%,rgba(10,14,40,.8) 100%)}
.svc-title{font-family:"Ubuntu",sans-serif;font-weight:700;font-size:16px;color:var(--white)}
.svc-sub{font-size:13px;color:#e8ebf2}

/* steps */
.steps{left:0;top:1986px;width:1200px;height:482px;background:var(--light-bg)}
.step-title{position:absolute;top:2316px;width:260px;text-align:center;font-family:"Ubuntu",sans-serif;font-weight:500;font-size:18px;color:var(--navy)}
.step-copy{position:absolute;top:2343px;width:260px;text-align:center;font-size:13.5px;line-height:20px;color:#8a8e99}

/* team */
.team-photo{left:0;top:2468px;width:1200px;height:535px;
  background:
    radial-gradient(ellipse 60px 90px at 36% 22%,rgba(205,165,140,.85),rgba(205,165,140,0)),
    radial-gradient(ellipse 110px 150px at 35% 20%,rgba(70,45,35,.6),rgba(70,45,35,0)),
    radial-gradient(ellipse 60px 160px at 35% 62%,rgba(40,60,120,.85),rgba(40,60,120,0)),
    radial-gradient(ellipse 170px 260px at 34% 75%,rgba(250,250,252,.95),rgba(250,250,252,0)),
    radial-gradient(ellipse 60px 200px at 12% 30%,rgba(150,190,210,.6),rgba(150,190,210,0)),
    linear-gradient(90deg,#eef1f3 0%,#dfe5ea 30%,#c9d3dc 55%)}
.team-item{position:absolute;left:630px;display:flex;align-items:center;gap:12px}
.team-icon{width:64px;height:64px;border-radius:50%;background:var(--white);display:flex;align-items:center;justify-content:center}
.team-item h4{font-family:"Ubuntu",sans-serif;font-weight:500;font-size:19px;color:var(--white)}
.team-item p{font-size:13px;color:#e4e8f1;margin-top:4px}

/* testimonials */
.avatar{position:absolute;border-radius:50%}
.quote-text{left:320px;top:3270px;width:560px;text-align:center;font-size:15.5px;line-height:23px;color:#8a8e99}
.arrow-btn{position:absolute;top:3431px;width:44px;height:44px;border-radius:50%;background:var(--navy);display:flex;align-items:center;justify-content:center}

/* footer */
.footer-links a{position:absolute;top:3828px;font-size:14px;font-weight:600;color:var(--white);text-decoration:none;transform:translateX(-50%)}
.contact{position:absolute;top:3924px;display:flex;align-items:center;gap:14px}
.contact-icon{width:58px;height:58px;border-radius:50%;border:1.5px solid var(--white);display:flex;align-items:center;justify-content:center}
.contact-text{font-size:12px;color:var(--white);line-height:18px}
.contact-text strong{font-size:14px;font-weight:600}
.footer-divider{position:absolute;top:3922px;width:1px;height:62px;background:#c9cde0}
.social{position:absolute;top:4028px;width:25px;height:25px;border:1.5px solid var(--white);border-radius:2px}
</style>
</head>
<body>

<!-- Top bar -->
<svg class="abs topbar" viewBox="0 0 1200 32" aria-hidden="true">
  <polygon points="430,0 1200,0 1200,32 403,32" fill="var(--navy)"/>
  <rect x="594" y="0" width="232" height="32" fill="#6c6c6c"/>
</svg>
<div class="abs topbar-text" style="left:445px;top:9px">
  <svg width="14" height="14" viewBox="0 0 24 24" fill="none" stroke="#fff" stroke-width="2"><path d="M22 16.9v3a2 2 0 0 1-2.2 2A19.8 19.8 0 0 1 2.1 4.2 2 2 0 0 1 4.1 2h3a2 2 0 0 1 2 1.7c.1 1 .4 1.9.7 2.8a2 2 0 0 1-.5 2.1L8 9.9a16 16 0 0 0 6 6l1.3-1.3a2 2 0 0 1 2.1-.4c.9.3 1.8.6 2.8.7a2 2 0 0 1 1.8 2z"/></svg>
  512 - 555 - 0148
</div>
<div class="abs topbar-text" style="left:626px;top:9px">
  <svg width="16" height="12" viewBox="0 0 24 18" fill="none" stroke="#fff" stroke-width="2"><rect x="1" y="1" width="22" height="16" rx="2"/><path d="M1 2l11 8 11-8"/></svg>
  REQUEST AN APPOINTMENT
</div>
<div class="abs topbar-text" style="left:858px;top:9px">
  <svg width="12" height="14" viewBox="0 0 20 24" fill="none" stroke="#fff" stroke-width="2"><path d="M10 23s8-7 8-13a8 8 0 0 0-16 0c0 6 8 13 8 13z"/><circle cx="10" cy="10" r="3"/></svg>
  88 Alder Lane Fairview
</div>

<!-- Header -->
<div class="abs logo" style="left:126px;top:36px"><span>VELMO</span><span class="logo-mark"></span></div>
<nav class="nav">
  <a style="left:396px;font-weight:700">Home</a>
  <a style="left:471px">About Us</a>
  <a style="left:546px">Treatments</a>
  <a style="left:634px">New Patients</a>
  <a style="left:729px">Fees</a>
  <a style="left:782px">Contact Us</a>
</nav>
<div class="abs book">BOOK ONLINE</div>

<!-- Hero -->
<div class="abs hero-photo" role="img" aria-label="Clinician in a mask treating a smiling senior patient in a teal treatment chair"></div>
<div class="abs hero-kicker">LEADERS IN IV</div>
<h1 class="abs hero-title">Potent Nutrition</h1>
<div class="abs hero-rule"></div>
<p class="abs hero-copy">Lorem ipsum dolor sit amet, consectetur adipiscing elit, sed do ei usmod tempor incididunt ut lab</p>
<div class="btn-pill" style="left:104px;width:145px;background:#5e5e5e">LEARN MORE</div>
<div class="btn-pill" style="left:259px;width:182px;background:var(--navy)">REQUEST QUOTE</div>
<svg class="abs" style="left:0;top:690px" width="1200" height="90" viewBox="0 0 1200 90" aria-hidden="true">
  <path d="M0 40 C250 5 450 5 700 30 C900 50 1050 55 1200 15 L1200 90 L0 90Z" fill="#6f6f6f"/>
  <path d="M0 45 C260 15 460 20 690 45 C880 65 1040 80 1200 60 L1200 90 L0 90Z" fill="#fff"/>
</svg>

<!-- About -->
<div class="abs center" style="top:845px"><span class="eyebrow">About us</span></div>
<h2 class="abs heading center" style="top:884px;font-size:41px">Who We Are</h2>
<div class="abs about-photo" role="img" aria-label="Smiling clinical team in blue scrubs and masks with a patient"></div>
<div class="abs about-card">
  <h3>Vital Nutrients, Amplified Wellness</h3>
  <p>Lorem ipsum dolor sit amet, consectetur adipiscing elit, sed do eiusmod tempor incididunt ut labore et dolore magna aliqua. Ut enim ad minim veniam, quis nostrud exercitation ullamco laboris nisi ut aliquip ex ea commodo consequat. Duis aute irure dolor in reprehenderit in voluptate velit esse cillum dolore eu fugiat nulla pariatur. Excepteur sint occaecat cupidatat</p>
</div>
<div class="btn btn-green" style="left:595px;top:1220px;width:157px;height:45px">Contact us
  <svg width="18" height="14" viewBox="0 0 18 14" fill="none" stroke="#fff" stroke-width="2"><path d="M1 7h15M10 1l6 6-6 6"/></svg>
</div>

<!-- Services -->
<div class="abs services" role="img" aria-label="Background of smiling patients and clinicians with a navy overlay"></div>
<div class="abs center" style="top:1488px"><span class="eyebrow" style="color:#fff;border-color:#fff;font-size:13px">Our services</span></div>
<h2 class="abs heading center" style="top:1525px;font-size:41px;color:#fff">Services We Offer</h2>

<div class="svc-card" style="left:140px;background:radial-gradient(ellipse 60px 50px at 38% 25%,rgba(230,225,190,.55),rgba(230,225,190,0)),radial-gradient(ellipse 60px 50px at 68% 28%,rgba(225,215,180,.5),rgba(225,215,180,0)),linear-gradient(180deg,#9cbb45,#86a838)" role="img" aria-label="Senior couple with a green overlay">
  <div style="position:absolute;left:0;top:78px;width:304px;text-align:center">
    <div class="svc-title">Performance Boosters</div>
    <div class="svc-sub" style="width:210px;margin:6px auto 0;line-height:20px">Lorem ipsum dolor sit amet, con sectetur adipiscing elit, sed do eiusmod tempor</div>
    <svg width="28" height="14" viewBox="0 0 28 14" fill="none" stroke="#fff" stroke-width="1.6" style="margin-top:6px"><path d="M1 7h25M20 1l6 6-6 6"/></svg>
  </div>
</div>
<div class="svc-card" style="left:467px;background:radial-gradient(ellipse 80px 80px at 48% 50%,rgba(235,195,170,.95),rgba(235,195,170,0)),radial-gradient(ellipse 110px 70px at 45% 15%,rgba(40,110,150,.8),rgba(40,110,150,0)),radial-gradient(ellipse 90px 60px at 50% 80%,rgba(240,240,242,.9),rgba(240,240,242,0)),linear-gradient(160deg,#8fb2c8,#c9b6a2 60%,#7a7880)" role="img" aria-label="Laughing child patient in a clinic">
  <div class="shade"></div>
  <svg style="position:absolute;left:34px;top:160px" width="30" height="30" viewBox="0 0 30 30" fill="none" stroke="var(--green-light)" stroke-width="2"><path d="M9 4h8M13 4v8l-7 12a2 2 0 0 0 2 3h14a2 2 0 0 0 2-3l-7-12V4"/></svg>
  <div style="position:absolute;left:84px;top:162px"><div class="svc-title">Hydration Therapy</div><div class="svc-sub" style="margin-top:6px">Lorem ipsum dolor sit amet</div></div>
</div>
<div class="svc-card" style="left:794px;background:radial-gradient(ellipse 100px 130px at 70% 45%,rgba(250,250,252,.95),rgba(250,250,252,0)),radial-gradient(ellipse 50px 50px at 68% 10%,rgba(200,170,150,.8),rgba(200,170,150,0)),radial-gradient(ellipse 40px 200px at 10% 40%,rgba(90,110,130,.7),rgba(90,110,130,0)),linear-gradient(160deg,#b8c2cc,#dfe3e7 50%,#5e6876)" role="img" aria-label="Senior doctor with a stethoscope at a desk">
  <div class="shade"></div>
  <svg style="position:absolute;left:34px;top:160px" width="30" height="30" viewBox="0 0 30 30" fill="none" stroke="var(--green-light)" stroke-width="2"><path d="M9 4h8M13 4v8l-7 12a2 2 0 0 0 2 3h14a2 2 0 0 0 2-3l-7-12V4"/></svg>
  <div style="position:absolute;left:84px;top:162px"><div class="svc-title">Detox Infusions</div><div class="svc-sub" style="margin-top:6px">Lorem ipsum dolor sit amet</div></div>
</div>
<div class="btn btn-green" style="left:542px;top:1893px;width:154px;height:45px">Contact us
  <svg width="18" height="14" viewBox="0 0 18 14" fill="none" stroke="#fff" stroke-width="2"><path d="M1 7h15M10 1l6 6-6 6"/></svg>
</div>

<!-- Steps -->
<div class="abs steps"></div>
<div class="abs center" style="top:2043px"><span class="eyebrow" style="font-size:13px">Steps</span></div>
<h2 class="abs heading center" style="top:2082px;font-size:41px">Simple Steps</h2>
<svg class="abs" style="left:0;top:2170px" width="1200" height="140" viewBox="0 0 1200 140" aria-hidden="true">
  <line x1="358" y1="69" x2="558" y2="69" stroke="var(--green)" stroke-width="2"/>
  <line x1="674" y1="69" x2="874" y2="69" stroke="var(--green)" stroke-width="2"/>
  <g id="step">
    <circle cx="300" cy="69" r="58" fill="none" stroke="var(--green)" stroke-width="2"/>
    <circle cx="300" cy="69" r="48" fill="var(--navy)"/>
    <path d="M292 50h14M299 50v14l-12 18a2 2 0 0 0 2 3h22a2 2 0 0 0 2-3l-12-18V50" fill="none" stroke="#fff" stroke-width="2.4"/>
    <circle cx="355" cy="69" r="12" fill="var(--green)"/>
    <text x="355" y="73" font-family="Open Sans,sans-serif" font-size="11" font-weight="700" fill="#fff" text-anchor="middle">01</text>
  </g>
  <use href="#step" x="316"/>
  <use href="#step" x="632"/>
</svg>
<div class="step-title" style="left:170px">Contact Us to Start</div>
<div class="step-copy" style="left:170px">Lorem ipsum dolor sit amet, consectetur adipiscing elit, sed do eiusmod</div>
<div class="step-title" style="left:486px">Set Up an Appointment</div>
<div class="step-copy" style="left:486px">Lorem ipsum dolor sit amet, consectetur adipiscing elit, sed do eiusmod</div>
<div class="step-title" style="left:802px">Get Assigned an Expert</div>
<div class="step-copy" style="left:802px">Lorem ipsum dolor sit amet, consectetur adipiscing elit, sed do eiusmod</div>

<!-- Team -->
<div class="abs team-photo" role="img" aria-label="Smiling female doctor in a white coat holding a tablet in a bright clinic"></div>
<svg class="abs" style="left:0;top:2468px" width="1200" height="535" viewBox="0 0 1200 535" aria-hidden="true">
  <polygon points="379,0 1200,0 1200,535 647,535" fill="var(--navy-soft)"/>
</svg>
<div class="abs" style="left:630px;top:2553px;font-size:13px;color:var(--green-light)">WHO WE ARE</div>
<h2 class="abs heading" style="left:630px;top:2588px;font-size:41px;line-height:54px;color:#fff">The team you can trust<br>to get the job done</h2>
<div class="team-item" style="top:2719px">
  <div class="team-icon"><svg width="30" height="30" viewBox="0 0 30 30" fill="none" stroke="var(--green)" stroke-width="2"><polygon points="15,3 27,12 22,27 8,27 3,12"/></svg></div>
  <div><h4>On-Time Appointments</h4><p>Lorem ipsum dolor sit amet, consectetur sipid</p></div>
</div>
<div class="team-item" style="top:2804px">
  <div class="team-icon"><svg width="30" height="30" viewBox="0 0 30 30" fill="none" stroke="var(--green)" stroke-width="2"><polygon points="15,3 27,12 22,27 8,27 3,12"/></svg></div>
  <div><h4>Client Centric</h4><p>Lorem ipsum dolor sit amet, consectetur sipid</p></div>
</div>
<div class="team-item" style="top:2886px">
  <div class="team-icon"><svg width="30" height="30" viewBox="0 0 30 30" fill="none" stroke="var(--green)" stroke-width="2"><polygon points="15,3 27,12 22,27 8,27 3,12"/></svg></div>
  <div><h4>Experienced Professionals</h4><p>Lorem ipsum dolor sit amet, consectetur sipid</p></div>
</div>

<!-- Testimonials -->
<div class="abs center" style="top:3059px"><span class="eyebrow" style="font-size:13px">Testimonials</span></div>
<h2 class="abs heading center" style="top:3098px;font-size:41px">Client Reviews</h2>
<div class="avatar" style="left:91px;top:3250px;width:100px;height:100px;background:radial-gradient(circle at 50% 70%,#2b2b30 0 30%,#a58a6e 31%)" role="img" aria-label="Client portrait"></div>
<div class="avatar" style="left:240px;top:3193px;width:60px;height:60px;background:linear-gradient(160deg,#e8e6e3,#c9c2bb)" role="img" aria-label="Client portrait"></div>
<div class="avatar" style="left:261px;top:3310px;width:40px;height:40px;background:linear-gradient(160deg,#e3e7ec,#9aa6b6)" role="img" aria-label="Client portrait"></div>
<div class="avatar" style="left:172px;top:3384px;width:82px;height:82px;background:linear-gradient(160deg,#efe7df,#c9a58e)" role="img" aria-label="Client portrait"></div>
<div class="avatar" style="left:892px;top:3179px;width:50px;height:50px;background:linear-gradient(160deg,#a2a5a9,#5f6266)" role="img" aria-label="Client portrait"></div>
<div class="avatar" style="left:1003px;top:3237px;width:104px;height:104px;background:linear-gradient(160deg,#f0f0f0,#c9c9cb)" role="img" aria-label="Client portrait"></div>
<div class="avatar" style="left:873px;top:3351px;width:60px;height:60px;background:linear-gradient(160deg,#f6cf8a,#e9a957)" role="img" aria-label="Client portrait"></div>
<div class="avatar" style="left:996px;top:3387px;width:82px;height:82px;background:linear-gradient(160deg,#f1eee8,#d3c9b8)" role="img" aria-label="Client portrait"></div>
<svg class="abs" style="left:589px;top:3191px" width="60" height="60" viewBox="0 0 60 60" aria-hidden="true">
  <circle cx="30" cy="30" r="30" fill="var(--green)"/>
  <text x="30" y="46" font-family="Ubuntu,sans-serif" font-size="40" font-weight="700" fill="#fff" text-anchor="middle">”</text>
</svg>
<p class="abs quote-text">Lorem ipsum dolor sit amet, consectetur adipiscing elit, sed do eiusmod tempor incididunt ut labore et dolore magna aliqua. Ut enim ad minim veniam, quis nostrud exercitation ullamco laboris nisi ut aliquip ex ea comm odo consequat. Duis aute irure</p>
<div class="abs center" style="top:3373px;font-size:13px;color:#6a6e79">Nolan Reyes</div>
<div class="abs center" style="top:3395px;font-size:11px;color:#8a8e99">Client</div>
<div class="arrow-btn" style="left:569px"><svg width="12" height="14" viewBox="0 0 12 14" fill="none" stroke="#fff" stroke-width="2"><path d="M3 1l6 6-6 6"/></svg></div>
<div class="arrow-btn" style="left:624px"><svg width="12" height="14" viewBox="0 0 12 14" fill="none" stroke="#fff" stroke-width="2"><path d="M9 1L3 7l6 6"/></svg></div>

<!-- Footer -->
<svg class="abs" style="left:0;top:3560px" width="1200" height="506" viewBox="0 0 1200 506" aria-hidden="true">
  <path d="M0 45 C300 -5 700 5 950 30 C1080 42 1150 40 1200 30 L1200 506 L0 506Z" fill="var(--green)"/>
  <path d="M0 82 C300 30 700 40 950 62 C1080 72 1150 68 1200 58 L1200 506 L0 506Z" fill="var(--navy)"/>
</svg>
<div class="abs logo" style="left:0;width:1200px;top:3718px;justify-content:center;color:#fff;font-size:46px"><span>VELMO</span><span class="logo-mark"></span></div>
<nav class="footer-links">
  <a style="left:374px">HOME</a>
  <a style="left:477px">SERVICES</a>
  <a style="left:586px">ABOUT US</a>
  <a style="left:720px">TESTIMONIALS</a>
  <a style="left:840px">BLOG</a>
</nav>
<div class="abs" style="left:142px;top:3878px;width:916px;height:1px;background:#8f93ad"></div>

<div class="contact" style="left:171px">
  <div class="contact-icon"><svg width="28" height="28" viewBox="0 0 24 24" fill="none" stroke="#fff" stroke-width="1.5"><circle cx="12" cy="12" r="10"/><path d="M2 12h20M12 2a15 15 0 0 1 0 20M12 2a15 15 0 0 0 0 20"/></svg></div>
  <div class="contact-text">123, Building Name, Street<br>City, State XY 123456</div>
</div>
<div class="footer-divider" style="left:429px"></div>
<div class="contact" style="left:505px">
  <div class="contact-icon"><svg width="22" height="28" viewBox="0 0 16 24" fill="none" stroke="#fff" stroke-width="1.5"><rect x="2" y="1" width="12" height="22" rx="2"/><path d="M6 19h4"/></svg></div>
  <div class="contact-text"><strong>PHONE</strong><br>(123) 456 7890</div>
</div>
<div class="footer-divider" style="left:750px"></div>
<div class="contact" style="left:826px">
  <div class="contact-icon"><svg width="28" height="22" viewBox="0 0 24 18" fill="none" stroke="#fff" stroke-width="1.5"><rect x="1" y="1" width="22" height="16" rx="2"/><path d="M1 2l11 8 11-8"/></svg></div>
  <div class="contact-text"><strong>EMAIL</strong><br>info@velmo.example</div>
</div>

<div class="abs" style="left:0;top:4014px;width:1200px;height:52px;background:var(--green-light)"></div>
<div class="abs" style="left:147px;top:4032px;font-size:13px;font-weight:700;color:#fff">VELMO HYDRATION</div>
<div class="social" style="left:934px"></div>
<div class="social" style="left:966px"></div>
<div class="social" style="left:998px"></div>
<div class="social" style="left:1030px"></div>

</body>
</html>
```